Business Card Design Project

I need some business cards with the logo you did for us (attached)
I am looking for a coulourful yet serious business card

We do market research
on the back I want the logo

on the front my name : Corinne Valdessac
position : Manager
address : Brume Analytica Sarl - 27 Rue des tanneurs
1847 Glarency - Switzerland
corinne.valdessac@brumeanalytica.ch
Tel : +4122 934 07 58
Mob France :+33 671 42 8356
Mob Italy +39 347 520 8163

The tree of the logo could also be used alone

THE BACKGROUND COLOR ON THE FRONT HAS TO BE WHITE, ON THE BACK YU CAN TRY OHER COLOUR BUT HOMOGENEOUS (NOT EXPENSIVE TO PRINT)

Target Market(s)

multinational companies or other market research companies

Industry/Entity Type

Market Research

Requirements
Must have
• logo on the back
and all the info above

```html
<!DOCTYPE html>
<html lang="en">
<head>
<meta charset="utf-8">
<title>Brume Analytica – Business Card</title>
<link rel="stylesheet" href="https://fonts.googleapis.com/css2?family=Varela+Round&family=Carlito:wght@400;700&display=swap">
<style>
  :root {
    --backdrop: #2b2b2b;
    --card: #ffffff;
    --brand-pink: #cf1b5a;
    --wine: #9b1c2c;
    --wine-deep: #7e1522;
    --sun: #f7c600;
    --leaf: #9cc93a;
    --title-green: #1f9a45;
    --ink: #2a2a2a;
    --icon: #c4202f;
  }
  * { box-sizing: border-box; margin: 0; padding: 0; }
  html, body {
    width: 1200px;
    height: 900px;
    overflow: hidden;
    background: var(--backdrop);
  }
  .stage {
    width: 1200px;
    height: 900px;
    display: flex;
    align-items: center;
    justify-content: center;
    gap: 40px;
  }
  .card {
    position: relative;
    width: 540px;
    height: 310px;
    background: var(--card);
    border-radius: 22px;
    overflow: hidden;
  }
  .wordmark {
    font-family: "Varela Round", sans-serif;
    color: var(--brand-pink);
    font-weight: 400;
    letter-spacing: 0.5px;
    white-space: nowrap;
  }
  .card-front .wordmark {
    position: absolute;
    left: 30px;
    top: 52px;
    font-size: 38px;
    z-index: 1;
  }
  .holder {
    position: absolute;
    left: 330px;
    top: 50px;
    font-family: "Carlito", sans-serif;
    white-space: nowrap;
    z-index: 1;
  }
  .holder-name {
    color: var(--wine);
    font-weight: 700;
    font-size: 18px;
  }
  .holder-role {
    color: var(--title-green);
    font-size: 16px;
    margin-left: 22px;
  }
  .contact {
    position: absolute;
    left: 30px;
    top: 138px;
    list-style: none;
    font-family: "Carlito", sans-serif;
    font-size: 12.5px;
    line-height: 16px;
    color: var(--ink);
    z-index: 1;
  }
  .contact li {
    display: flex;
    align-items: center;
    gap: 6px;
    white-space: nowrap;
  }
  .contact li.indent { padding-left: 14px; }
  .contact svg { width: 8px; height: 8px; fill: var(--icon); flex: none; }
  .swoosh {
    position: absolute;
    inset: 0;
    width: 540px;
    height: 310px;
  }
  .card-back {
    display: flex;
    align-items: center;
    justify-content: center;
  }
  .card-back .wordmark { font-size: 46px; }
</style>
</head>
<body>
<main class="stage">
  <section class="card card-front" aria-label="Card front">
    <svg class="swoosh" viewBox="0 0 540 310" aria-hidden="true">
      <path fill="var(--leaf)" d="M230,236 C370,200 480,136 540,40 V66 C470,150 360,210 230,236 Z"/>
      <path fill="var(--sun)" d="M0,272 C180,250 420,180 540,80 V310 H0 Z"/>
      <path fill="var(--wine)" d="M0,294 C170,274 420,210 540,116 V310 H0 Z"/>
    </svg>

    <div class="wordmark">brume analytica</div>

    <div class="holder">
      <div class="holder-name">Corinne Valdessac</div>
      <div class="holder-role">Manager</div>
    </div>

    <ul class="contact">
      <li><svg viewBox="0 0 10 10"><path d="M5 0 L10 5 H8.5 V10 H1.5 V5 H0 Z"/></svg>Brume Analytica Sarl - 27 Rue des tanneurs</li>
      <li class="indent">1847 Glarency - Switzerland</li>
      <li><svg viewBox="0 0 10 10"><rect x="0" y="2" width="10" height="7" rx="1"/></svg>corinne.valdessac@brumeanalytica.ch</li>
      <li><svg viewBox="0 0 10 10"><rect x="1" y="0" width="8" height="10" rx="1.5"/></svg>+4122 934 07 58</li>
      <li><svg viewBox="0 0 10 10"><rect x="2" y="0" width="6" height="10" rx="1.2"/></svg>+33 671 42 8356</li>
      <li><svg viewBox="0 0 10 10"><rect x="2" y="0" width="6" height="10" rx="1.2"/></svg>+39 347 520 8163</li>
    </ul>
  </section>

  <section class="card card-back" aria-label="Card back">
    <div class="wordmark">brume analytica</div>
  </section>
</main>
</body>
</html>
```